Fun Language School in San Diego, CA - We want cool Business Card

We need a new business card design for our new logo. We are a language school in beautiful San Diego, California. Our target is students from all over the world who age from 18 to 25. They come to our school to learn English. Our school has a modern look, trending and fun place. We are the only language school who use tablets in class. We are student oriented, Students Come First is our slogan. We are re-branding ourselves with a new logo. We would like to see a designs that use our new logo and it should reflect the feel of young, fun, modern, high-tech and attractive to young people.
I've seen some business card designs with transparent look, unusual shapes, we are open to any cool ideas. Thank you very much!

In order for you to know more about our school, here are the links to our Youtube Channel and Facebook.

Youtube: https://www.vidloop.example/channel/ZXpo84kR-21bvn5wQ7t2LmHd
Facebook: https://www.friendspace.example/TVSchool

Target Market(s)

Our target is students from all over the world who age from 18 to 25. International students.

Industry/Entity Type

School

Font styles to use
Sans Serif

Requirements
Must have
• Our new logo. Name, title and address.
Should not have
• Other colors other than the ones we have in our logo. Characters are fine.

```html
<!DOCTYPE html>
<html lang="en">
<head>
<meta charset="utf-8">
<title>Harborline School – Business Card</title>
<link rel="stylesheet" href="https://fonts.googleapis.com/css2?family=Montserrat:wght@500&family=Jura:wght@500&display=swap">
<style>
  :root {
    --page: #f2f0ec;
    --card: #e7e4df;
    --blue: #5a9ec6;
    --lime: #d4e04a;
    --teal: #3bb3b8;
    --ink-grey: #767676;
    --white: #ffffff;
  }
  html, body {
    margin: 0;
    padding: 0;
    width: 1200px;
    height: 769px;
    overflow: hidden;
    background: var(--page);
  }
  .canvas {
    position: relative;
    width: 1200px;
    height: 769px;
  }
  .business-card {
    position: absolute;
    left: 160px;
    top: 130px;
    width: 880px;
    height: 508px;
    border-radius: 22px;
    background: var(--card);
    overflow: hidden;
    box-shadow: 0 2px 10px rgba(0,0,0,0.08);
  }
  .card-bands {
    position: absolute;
    inset: 0;
  }
  .brand {
    position: absolute;
    left: 205px;
    top: 96px;
    display: flex;
    align-items: center;
    gap: 18px;
  }
  .brand-dot {
    width: 58px;
    height: 58px;
    border-radius: 50%;
    background: var(--teal);
    flex: none;
  }
  .brand-name {
    font-family: "Montserrat", sans-serif;
    font-weight: 500;
    color: var(--ink-grey);
    font-size: 46px;
    line-height: 1;
    letter-spacing: 0.2px;
  }
  .divider {
    position: absolute;
    left: 440px;
    top: 255px;
    width: 1.5px;
    height: 158px;
    background: var(--white);
  }
  .contact-list {
    position: absolute;
    left: 506px;
    top: 270px;
    margin: 0;
    padding: 0;
    list-style: none;
    font-family: "Jura", sans-serif;
    font-weight: 500;
    font-size: 14.5px;
    letter-spacing: 0.6px;
    color: var(--white);
    white-space: nowrap;
  }
  .contact-item {
    display: flex;
    align-items: center;
    gap: 9px;
    height: 26.7px;
  }
  .contact-icon {
    width: 17px;
    height: 17px;
    flex: none;
  }
</style>
</head>
<body>
<div class="canvas">
  <div class="business-card">
    <svg class="card-bands" width="880" height="508" viewBox="0 0 880 508" aria-hidden="true">
      <path d="M0,198 Q440,284 880,198 L880,462 Q440,394 0,462 Z" fill="var(--blue)"/>
      <path d="M0,190 Q440,276 880,190" fill="none" stroke="var(--lime)" stroke-width="6"/>
      <path d="M0,470 Q440,402 880,470" fill="none" stroke="var(--lime)" stroke-width="6"/>
    </svg>

    <div class="brand">
      <span class="brand-dot"></span>
      <span class="brand-name">Harborline School</span>
    </div>

    <div class="divider"></div>

    <ul class="contact-list">
      <li class="contact-item">
        <svg class="contact-icon" viewBox="0 0 16 16"><circle cx="8" cy="8" r="8" fill="#fff"/><path d="M5.2,4 L6.8,4 L7.3,6 L6.3,6.8 Q7.2,8.8 9.2,9.7 L10,8.7 L12,9.2 L12,10.8 Q8,11.5 5,7.5 Q4.6,5.5 5.2,4 Z" fill="var(--blue)"/></svg>
        <span>619 555 0142</span>
      </li>
      <li class="contact-item">
        <svg class="contact-icon" viewBox="0 0 16 16"><circle cx="8" cy="8" r="8" fill="#fff"/><rect x="5.5" y="3.5" width="5" height="9" rx="1" fill="var(--blue)"/><rect x="6.3" y="4.6" width="3.4" height="5.8" fill="#fff"/></svg>
        <span>619 555 0187</span>
      </li>
      <li class="contact-item">
        <svg class="contact-icon" viewBox="0 0 16 16"><circle cx="8" cy="8" r="8" fill="#fff"/><rect x="4" y="5.3" width="8" height="5.6" fill="var(--blue)"/><path d="M4,5.3 L8,8.5 L12,5.3" fill="none" stroke="#fff" stroke-width="0.9"/></svg>
        <span>hello@harborline.example</span>
      </li>
      <li class="contact-item">
        <svg class="contact-icon" viewBox="0 0 16 16"><circle cx="8" cy="8" r="8" fill="#fff"/><g fill="none" stroke="var(--blue)" stroke-width="0.9"><circle cx="8" cy="8" r="4.6"/><ellipse cx="8" cy="8" rx="2" ry="4.6"/><line x1="3.4" y1="8" x2="12.6" y2="8"/></g></svg>
        <span>www.harborline.example</span>
      </li>
      <li class="contact-item">
        <svg class="contact-icon" viewBox="0 0 16 16"><circle cx="8" cy="8" r="8" fill="#fff"/><path d="M8,13 Q4.6,8.8 4.6,6.8 A3.4,3.4 0 0 1 11.4,6.8 Q11.4,8.8 8,13 Z" fill="var(--blue)"/><circle cx="8" cy="6.8" r="1.3" fill="#fff"/></svg>
        <span>18th floor, 2140 Bayfront Ave, San Diego</span>
      </li>
    </ul>
  </div>
</div>
</body>
</html>
```